IT support company needs Banner Ad for the top of their quote layout template

We need a banner Ad for the top of our for quote layout template so it is sent out on all our quotes

The banner size must be 827 x 100 pixels - anything larger than 60 KB can cause upload time issues

We have attached our logo and examples of the quote page to see how it looks in the context of the whole page.

Essential elements of the banner
- Must have our logo but this can be changed to be different colours if it makes the design work better i.e. Tidal Grove could be all in white

Colours
- Can use all of our standard colours - Orange, Black, Grey and White

Images
- As a premium IT support company we deal with people and technology so would like to see both of these Incorporated into the banner i.e. people using technology These images could be watermarked or one colour effect.

Look and Feel
- Professional, friendly, people, technology, premium

Target Market
Small business owners and managers

Industry/Entity Type

It Company

```html
<!DOCTYPE html>
<html lang="en">
<head>
<meta charset="utf-8">
<title>Tidal Grove Quote</title>
<link href="https://fonts.googleapis.com/css2?family=Archivo+Black&family=Carlito:wght@400;700&display=swap" rel="stylesheet">
<style>
:root{
  --orange:#f26522;
  --orange-deep:#e0521a;
  --ink:#111;
  --blue:#1a73c4;
  --rule:#2a6fb8;
  --head-a:#a9d3f2;
  --head-b:#e4f2fc;
  --row-alt:#f4f6f7;
  --dark:#2b2420;
}
html,body{margin:0;width:1200px;height:1200px;overflow:hidden;background:#fff}
.stage{position:absolute;left:0;top:0;width:1500px;height:1500px;transform:scale(.8);transform-origin:0 0;font-family:"Carlito",sans-serif;color:var(--ink)}
.page{position:absolute;left:288px;top:140px;width:881px;height:1190px;background:#fff;border:1px solid #333;box-sizing:border-box;overflow:hidden}
.abs{position:absolute}
.banner{left:0;top:0;width:880px;height:106px}
.brand{left:28px;top:40px;font-weight:700;font-size:21px;color:var(--dark);letter-spacing:.5px}
.tagline{left:260px;top:24px;font-family:"Archivo Black",sans-serif;font-size:22px;line-height:25px;color:#fff;letter-spacing:.8px;white-space:nowrap}
.tagline span{color:var(--orange);display:block;padding-left:3px}
.perks{left:592px;top:20px;margin:0;padding:0;list-style:none;font-family:"Archivo Black",sans-serif;font-size:14.5px;color:#fff;letter-spacing:.6px}
.perks li{height:24.5px;display:flex;align-items:center;gap:6px}
.doc-title{left:29px;top:148px;font-size:23px}
.portrait{left:28px;top:190px;width:104px;height:140px;background:linear-gradient(#5a5a5a,#8a8a8a 60%,#3c3c3c)}
.party{top:188px;font-size:14px;line-height:21px}
.party h3{margin:0 0 3px;font-weight:400;font-size:17.5px;color:var(--blue)}
.party b{font-weight:700}
.top-rule{left:27px;top:342px;width:826px;height:3px;background:var(--rule)}
.section{left:29px;font-size:20px}
table{position:absolute;left:27px;width:826px;border-collapse:collapse;border:2px solid #222;font-size:14.5px}
th{font-weight:400;height:25px;padding:0 5px;background:linear-gradient(90deg,var(--head-a),var(--head-b) 45%,var(--head-a));text-align:left;border-bottom:1px solid #222}
td{height:27px;padding:0 5px}
tr:nth-child(odd):not(:first-child) td{background:var(--row-alt)}
.num{text-align:right}
.col{border-left:1.5px solid #222}
.sum{left:27px;width:821px;display:flex;justify-content:flex-end;font-size:14.5px;height:20px}
.sum .lbl{color:var(--blue);margin-right:54px}
.sum .val{font-weight:700;width:70px;text-align:right}
.note{left:29px;top:983px;font-size:14px}
.sign-line{top:1059px;height:1px;background:#222}
.sign-lbl{top:1062px;font-size:14px}
.foot-rule{left:0;top:1141px;width:879px;height:4px;background:linear-gradient(90deg,#2a6fb8,#41b3e6)}
.foot{left:0;top:1145px;width:879px;height:43px;background:linear-gradient(90deg,#fff,#b8e0f6 30%,#4fbbe9 60%,#b8e0f6 85%,#e9f5fc);font-size:14px}
.foot span{position:absolute;top:10px}
</style>
</head>
<body>
<div class="stage">
<div class="page">
  <svg class="abs banner" viewBox="0 0 880 106" aria-hidden="true">
    <defs>
      <linearGradient id="or" x1="0" x2="1"><stop offset="0" stop-color="#e8541b"/><stop offset=".6" stop-color="#f26522"/><stop offset="1" stop-color="#e9561e"/></linearGradient>
    </defs>
    <polygon points="575,0 880,0 880,106 508,106" fill="url(#or)"/>
  </svg>
  <div class="abs" role="img" aria-label="Close-up photograph of a laptop keyboard" style="left:162px;top:0;width:418px;height:106px;clip-path:polygon(68px 0,418px 0,350px 106px,0 106px);background:linear-gradient(120deg,#5a4536,#2a211b 55%,#4a3a2e)"></div>
  <div class="abs brand">Tidal Grove</div>
  <div class="abs tagline">Your Trusted Local<span>IT Partners</span></div>
  <ul class="abs perks">
    <li><svg width="14" height="12" viewBox="0 0 14 12"><path d="M1 6l4 4 8-9" stroke="#fff" stroke-width="2.6" fill="none"/></svg>Proactive Care</li>
    <li><svg width="14" height="12" viewBox="0 0 14 12"><path d="M1 6l4 4 8-9" stroke="#fff" stroke-width="2.6" fill="none"/></svg>Round the Clock Maintenance</li>
    <li><svg width="14" height="12" viewBox="0 0 14 12"><path d="M1 6l4 4 8-9" stroke="#fff" stroke-width="2.6" fill="none"/></svg>Live Help Desk Support</li>
  </ul>

  <div class="abs doc-title">Standard MSP&nbsp; #2</div>
  <div class="abs portrait" role="img" aria-label="Portrait photograph of the quote author"></div>
  <div class="abs party" style="left:144px"><h3>Opgesteld door:</h3><b>Marcus Hale Inc</b><br>Marcus Hale<br><br>Fax<br>marcus.hale@quotewell.com</div>
  <div class="abs party" style="left:384px"><h3>Opgesteld voor:</h3><b>Copper Ridge</b><br>218 Alder Rd.<br>Fairview,&nbsp;&nbsp; 40721<br>Laura Penn<br>l.penn@bluefinch.co.uk</div>
  <div class="abs party" style="left:668px"><h3>Gegevens Offerte:</h3><b>Offerte #: MH-000280</b><br>Versie: 1<br>Leverdatum: 14/11/2017<br>Vervaldatum: 31/12/2017</div>
  <div class="abs top-rule"></div>

  <div class="abs section" style="top:363px">Overzicht Offerte</div>
  <table style="top:392px">
    <tr><th>Beschrijving</th><th class="num col" style="width:104px">Bedrag</th></tr>
    <tr><td>Initial Investment</td><td class="num col">$800.00</td></tr>
  </table>
  <div class="abs sum" style="top:456px"><span class="lbl">Subtotaal:</span><span class="val">$800.00</span></div>
  <div class="abs sum" style="top:483px"><span class="lbl">VAT:</span><span class="val">$160.00</span></div>
  <div class="abs sum" style="top:510px"><span class="lbl">Totaal:</span><span class="val">$960.00</span></div>

  <div class="abs section" style="top:552px">Overzicht Terugkerende Kosten</div>
  <table style="top:580px">
    <tr><th>Beschrijving</th><th class="num col" style="width:104px">Bedrag</th></tr>
    <tr><td>Monitoring</td><td class="num col">$375.00</td></tr>
    <tr><td>Support</td><td class="num col">$65.00</td></tr>
    <tr><td>Fixed Hours</td><td class="num col">$850.00</td></tr>
  </table>
  <div class="abs sum" style="top:699px"><span class="lbl">Terugkerende totaal:</span><span class="val">$1,290.00</span></div>

  <div class="abs section" style="top:741px">*Optionele kosten</div>
  <table style="top:769px">
    <tr><th>Beschrijving</th><th class="num col" style="width:105px">Recurring</th><th class="num col" style="width:104px">One-Time</th></tr>
    <tr><td>Monitoring</td><td class="num col">$790.00</td><td class="num col">$0.00</td></tr>
    <tr><td>Support</td><td class="num col">$185.00</td><td class="num col">$0.00</td></tr>
    <tr><td>Fixed Hours</td><td class="num col">$695.00</td><td class="num col">$0.00</td></tr>
    <tr><td>Add-on Services</td><td class="num col">$850.00</td><td class="num col">$0.00</td></tr>
  </table>
  <div class="abs sum" style="top:916px"><span class="lbl">Optionele terugkerend bedrag:</span><span class="val">$2,520.00</span></div>
  <div class="abs sum" style="top:943px"><span class="lbl">Optionele ongeplande Subtotaal:</span><span class="val">$.00</span></div>

  <div class="abs note">Taxes, shipping, handling and other fees may apply.&nbsp; We reserve the right to cancel orders arising from pricing or other errors.</div>
  <div class="abs sign-line" style="left:27px;width:494px"></div>
  <div class="abs sign-line" style="left:552px;width:194px"></div>
  <div class="abs sign-lbl" style="left:29px">Handtekening</div>
  <div class="abs sign-lbl" style="left:554px">Datum</div>

  <div class="abs foot-rule"></div>
  <div class="abs foot"><span style="left:29px">Offerte #MH-000280 v1</span><span style="right:29px">Pagina 6 Van 7</span></div>
</div>
</div>
</body>
</html>
```